Redesign Of Facebook Page Banner and Profile image

I just want to redesign my facebook page to be not so busy....more clean professional dental look. I dont like stock images so much so please go down the newsfeed to use an image or two from it...so it looks personable.

https://www.pagenook.com/RVMolarCareCo/

Target Market(s)

Consumers that care about their looks

Industry/Entity Type

Dental Clinic

Requirements
Must have
• I just want to redesign my facebook page to be not so busy....more clean professional modern look. I don't like stock images so much so please go down the newsfeed to use an image or two from it...so it looks personable.
• https://www.pagenook.com/RVMolarCareCo/
Nice to have
• I just want to redesign my facebook page to be not so busy....more clean professional dental look. I dont like stock images so much so please go down the newsfeed to use an image or two from it...so it looks personable.
Should not have

```html
<!DOCTYPE html>
<html lang="en">
<head>
<meta charset="utf-8">
<title>Riverview Molar Care Co. – Page Cover and Profile</title>
<link rel="stylesheet" href="https://fonts.googleapis.com/css2?family=Source+Sans+3:wght@400;600;700&display=swap">
<style>
  :root {
    --page-bg: #ffffff;
    --ink-teal: #1b5d78;
    --accent-orange: #f7941d;
    --band-blue: #19a8dc;
    --band-blue-deep: #0e7fb0;
    --sky-light: #cdeef9;
    --sky-pale: #eef9fd;
    --photo-warm-light: #f1e3da;
    --photo-warm-mid: #dcbfae;
    --logo-grey: #b9c4cb;
    --logo-text: #3d4a52;
    --white: #ffffff;
  }
  * { box-sizing: border-box; margin: 0; padding: 0; }
  html, body {
    width: 1200px; height: 546px; overflow: hidden;
    background: var(--page-bg);
    font-family: "Source Sans 3", "Myriad Pro", Arial, sans-serif;
  }
  .canvas { position: relative; width: 1200px; height: 546px; }

  /* Profile image */
  .profile-tile {
    position: absolute; left: 102px; top: 81px; width: 180px; height: 180px;
    background: linear-gradient(135deg, var(--white) 30%, var(--sky-light) 100%);
    box-shadow: 0 2px 6px rgba(0,0,0,.25);
    display: flex; flex-direction: column; align-items: center;
  }
  .profile-mark {
    width: 72px; height: 72px; border-radius: 50%;
    margin-top: 24px;
    background: radial-gradient(circle at 40% 35%, #f4f7f9, var(--logo-grey));
  }
  .profile-name {
    margin-top: 16px; text-align: center;
    color: var(--logo-text); font-weight: 600; font-size: 19px; line-height: 1.05;
  }

  /* Cover banner */
  .cover {
    position: absolute; left: 306px; top: 82px; width: 833px; height: 318px;
    overflow: hidden;
    background: linear-gradient(100deg, var(--white) 52%, var(--sky-pale) 68%, var(--sky-light) 100%);
    box-shadow: 0 8px 10px -4px rgba(0,0,0,.3);
  }
  .cover-photo {
    position: absolute; left: 62px; top: 0; width: 280px; height: 290px;
    background: linear-gradient(160deg, var(--photo-warm-light), var(--photo-warm-mid));
    -webkit-mask-image: linear-gradient(90deg, transparent, #000 18%, #000 82%, transparent);
    mask-image: linear-gradient(90deg, transparent, #000 18%, #000 82%, transparent);
  }
  .cover-wave { position: absolute; left: 0; top: 0; width: 833px; height: 318px; }

  .offer { position: absolute; color: var(--ink-teal); font-weight: 600; white-space: nowrap; }
  .offer-line1 { left: 444px; top: 26px; font-size: 36px; }
  .offer-line2 { left: 444px; top: 68px; font-size: 36px; }
  .offer-reg { font-size: 16px; font-weight: 400; margin-left: 6px; }
  .offer-price {
    position: absolute; left: 662px; top: 26px;
    color: var(--accent-orange); font-weight: 600; font-size: 84px; line-height: 1;
  }
  .offer-service { left: 444px; top: 110px; font-size: 19.7px; }
  .offer-cta { left: 444px; top: 133px; font-size: 30px; color: var(--accent-orange); }

  .contact { position: absolute; color: var(--white); white-space: nowrap; }
  .contact-phone { left: 548px; top: 263px; font-size: 18px; font-weight: 600; display: flex; align-items: center; gap: 7px; }
  .contact-web { left: 464px; top: 288px; font-size: 19px; font-weight: 400; }
</style>
</head>
<body>
<div class="canvas">

  <div class="profile-tile">
    <div class="profile-mark"></div>
    <div class="profile-name">Riverview<br>Molar Care Co.</div>
  </div>

  <div class="cover">
    <div class="cover-photo" role="img" aria-label="Portrait photo of a smiling patient showing white teeth"></div>

    <svg class="cover-wave" viewBox="0 0 833 318" aria-hidden="true">
      <defs>
        <linearGradient id="bandGrad" x1="0" x2="1" y1="0" y2="0">
          <stop offset="0" stop-color="var(--band-blue)"/>
          <stop offset="1" stop-color="var(--band-blue-deep)"/>
        </linearGradient>
      </defs>
      <path d="M0 262 C180 300 330 285 470 240 C600 200 720 195 833 250 L833 318 L0 318 Z" fill="#dfe6ea"/>
      <path d="M0 250 C160 300 360 300 520 245 C640 205 740 210 833 265 L833 318 L0 318 Z" fill="var(--white)"/>
      <path d="M0 318 L0 245 C120 280 260 285 420 265 C580 245 720 240 833 285 L833 318 Z" fill="url(#bandGrad)"/>
    </svg>

    <div class="offer offer-line1">LIMITED TIME</div>
    <div class="offer offer-line2">SPECIAL<span class="offer-reg">(REG $378)</span></div>
    <div class="offer-price">$99</div>
    <div class="offer offer-service">PROFESSIONAL LASER TEETH WHITENING</div>
    <div class="offer offer-cta">SCHEDULE AN APPT TODAY</div>

    <div class="contact contact-phone">
      <svg width="17" height="17" viewBox="0 0 16 16" aria-hidden="true">
        <circle cx="8" cy="8" r="7" fill="none" stroke="var(--white)" stroke-width="1.4"/>
        <path d="M5.4 4.3l1.3 1.5-.7 1c.5 1 1.3 1.8 2.3 2.3l1-.7 1.5 1.3-.8 1.2C8 10.6 5.5 8.2 4.9 5.1z" fill="var(--white)"/>
      </svg>
      555 014 2368
    </div>
    <div class="contact contact-web">www.RiverviewMolarCare.com</div>
  </div>

</div>
</body>
</html>
```